Boutique custom software development company needs new business card

Our nearly 20 year old custom software development company would like to better include the fact that we are now providing Bitcoin services. These new services are B2B include education (how to acquire and securely hold Bitcoin) and integrating Bitcoin payments into existing ecommerce sites or other existing systems. Please keep the card clean and simple. Attached is our current design and some other files. vexalon.example

Target Market(s)

businesses owners interested in long term relationship

Industry/Entity Type

Custom software development and Bitcoin

Contact Information for Business Card

Marcus Ellwood, marcus@vexalon.example, vexalon.example, (888) 555-VEXAL

Font styles to use
Other font styles liked:
• monospace

Requirements
Must have
• double-sided
Nice to have
• clean and simple
Should not have
• physical address

```html
<!DOCTYPE html>
<html lang="en">
<head>
<meta charset="utf-8">
<title>Vexalon Business Card</title>
<link rel="stylesheet" href="https://fonts.googleapis.com/css2?family=Roboto+Mono:wght@400;700&family=Roboto:wght@700&family=Fira+Sans+Condensed:wght@600&display=swap">
<style>
  :root {
    --bg: #e4e4e2;
    --navy: #283580;
    --navy-glow: #3a55b8;
    --orange: #f49c27;
    --white: #ffffff;
    --icon-light: #dfe5f7;
    --icon-mid: #8fa2de;
  }
  * { margin: 0; padding: 0; box-sizing: border-box; }
  html, body {
    width: 1200px; height: 846px; overflow: hidden;
    background: var(--bg);
  }
  .canvas { position: relative; width: 1200px; height: 846px; }
  .card {
    position: absolute; left: 346px; width: 508px; height: 290px;
    background: var(--navy); overflow: hidden;
  }
  .card--front { top: 99px; }
  .card--back { top: 456px; }

  .wordmark {
    font-family: "Roboto Mono", monospace; font-weight: 700;
    letter-spacing: 1px; line-height: 1;
  }
  .card--front .wordmark {
    position: absolute; left: 55px; top: 71px; width: 205px;
    color: var(--white); font-size: 35px; text-align: center;
  }
  .divider {
    position: absolute; left: 277px; top: 53px; width: 1px; height: 70px;
    background: rgba(255,255,255,0.55);
  }
  .contact {
    position: absolute; left: 292px; top: 49px;
    font-family: "Roboto Mono", monospace; font-size: 15px;
    line-height: 19.4px; color: var(--white); list-style: none;
  }
  .contact .name { color: var(--orange); font-weight: 700; }

  .services {
    position: absolute; left: 0; top: 148px; width: 100%;
    display: flex; list-style: none;
  }
  .service {
    position: absolute; width: 110px; margin-left: -55px;
    display: flex; flex-direction: column; align-items: center;
  }
  .service:nth-child(1) { left: 72px; }
  .service:nth-child(2) { left: 193px; }
  .service:nth-child(3) { left: 315px; }
  .service:nth-child(4) { left: 436px; }
  .service-art {
    width: 72px; height: 72px; border-radius: 50%;
    background: radial-gradient(circle at 40% 35%, var(--icon-light) 0%, var(--icon-mid) 45%, var(--navy-glow) 75%, rgba(40,53,128,0) 100%);
  }
  .service-label {
    margin-top: 7px;
    font-family: "Fira Sans Condensed", sans-serif; font-weight: 600;
    font-size: 12px; line-height: 14.5px; color: var(--orange);
    text-align: center; text-transform: uppercase;
  }
  .accent-band {
    position: absolute; left: 0; bottom: 0; width: 100%; height: 14px;
    background: var(--orange);
  }

  .card--back .wordmark {
    position: absolute; left: 0; top: 98px; width: 100%;
    color: var(--orange); font-size: 52px; text-align: center;
  }
  .back-url {
    position: absolute; left: 0; top: 168px; width: 100%;
    font-family: "Roboto", sans-serif; font-weight: 700; font-size: 16px;
    letter-spacing: 0.5px; color: var(--orange); text-align: center;
  }
</style>
</head>
<body>
<main class="canvas">
  <section class="card card--front" aria-label="Card front">
    <div class="wordmark">VEXALON</div>
    <div class="divider"></div>
    <ul class="contact">
      <li class="name">Marcus Ellwood</li>
      <li>(888) 555-VEXAL</li>
      <li>marcus@vexalon.example</li>
      <li>www.vexalon.example</li>
    </ul>
    <ul class="services">
      <li class="service">
        <div class="service-art" role="img" aria-label="Illustration of an app panel with toggle switches"></div>
        <p class="service-label">Web &amp; Native<br>Applications</p>
      </li>
      <li class="service">
        <div class="service-art" role="img" aria-label="Illustration of a round robot head"></div>
        <p class="service-label">Digital Process<br>Automation</p>
      </li>
      <li class="service">
        <div class="service-art" role="img" aria-label="Illustration of a 3D cloud with data pattern"></div>
        <p class="service-label">Cloud-Based<br>Portals</p>
      </li>
      <li class="service">
        <div class="service-art" role="img" aria-label="Illustration of a glossy brain"></div>
        <p class="service-label">Bitcoin<br>Consulting</p>
      </li>
    </ul>
    <div class="accent-band"></div>
  </section>

  <section class="card card--back" aria-label="Card back">
    <div class="wordmark">VEXALON</div>
    <p class="back-url">WWW.VEXALON.EXAMPLE</p>
  </section>
</main>
</body>
</html>
```